Bakery Replacement Lighted Sign Face

We are opening a new bakery that sells only cakes. The name is "The Willow Lantern." We are replacing the current sign face with a new look that states our name and makes a bold statement of fun. We will be known for having 101 cakes that are always ready for immediate pickup or delivery. Our colors are pink, orange, and lime green. An image is provided to see the colors.

Target Market(s)

people who buy cakes for parties and all other occasions

Industry/Entity Type

Cakes

Other font styles liked:
• look at the logo and file for the main font name

Colors
59FF00
82FF00
B8FF75
E3FFCB
F4FFEA
F0912C
F2A743
F7CA91
FBE8D2
FDF5EE
EB3D1F
EC4F4E
F09395
F8D3D4
FCEDEE

Requirements
Must have
• The name of the bakery. Logo can be used as is or changed as shown in one of the uploaded PDFs. Must use either pink, orange, lime green, white, or black. We prefer a bright pink background with white lettering as our first choice, but are willing to be open minded to see all creative concepts. Also the sign is 14 feet long and 42 inches tall so the artwork must fit within those boundaries. Also keep in mind the sign does have a 4 inch black frame. So the graphics area is actually 13 feet 2 inches by 3 feet. Also, in the attached pdf that shows a rough possible layout, the words "101 cakes to go" is on the sign. It is NOT a must. Only use the wording if it adds to your design.
Nice to have
• You are welcome to add additional stars or other fun graphics that could look good.
Should not have
• No images of cakes or other bakery products.

```html
<!DOCTYPE html>
<html lang="en">
<head>
<meta charset="utf-8">
<title>The Willow Lantern – Sign Face</title>
<link rel="stylesheet" href="https://fonts.googleapis.com/css2?family=Fredoka:wght@600&display=swap">
<style>
  :root {
    --backdrop: #404040;
    --sign-pink: #ef7879;
    --doodle-pink: #e4585e;
    --badge-white: #ffffff;
    --badge-orange: #ec6a2c;
    --star-orange: #ef6d2e;
    --star-edge: #d63a2a;
    --name-pink: #f07e82;
    --rule-green: #3fb33a;
  }
  html, body {
    margin: 0;
    padding: 0;
    width: 1200px;
    height: 691px;
    overflow: hidden;
    background: var(--backdrop);
  }
  .sign {
    display: block;
    width: 1200px;
    height: 691px;
  }
  .sign-face { fill: var(--sign-pink); }
  .doodle { fill: var(--doodle-pink); opacity: 0.45; }
  .fun-star { fill: var(--star-orange); stroke: var(--star-edge); stroke-width: 1.5; stroke-linejoin: round; }
  .badge-edge { fill: var(--badge-white); }
  .badge-ring { fill: var(--badge-orange); }
  .badge-dots { fill: none; stroke: var(--badge-white); stroke-width: 3.5; stroke-linecap: round; stroke-dasharray: 0 11; }
  .badge-center { fill: var(--badge-white); }
  .badge-rule { fill: none; stroke: var(--rule-green); stroke-width: 1.2; }
  .bakery-name {
    font-family: "Fredoka", sans-serif;
    font-weight: 600;
    font-size: 58px;
    fill: var(--name-pink);
    text-anchor: middle;
  }
</style>
</head>
<body>
<svg class="sign" viewBox="0 0 1200 691" xmlns="http://www.w3.org/2000/svg" aria-label="The Willow Lantern sign face">
  <defs>
    <clipPath id="sign-area">
      <rect x="99" y="190" width="1002" height="250"/>
    </clipPath>
  </defs>

  <g clip-path="url(#sign-area)">
    <rect class="sign-face" x="99" y="190" width="1002" height="250"/>

    <rect class="doodle" x="139" y="214" width="63" height="74" rx="18" role="img" aria-label="Line drawing of a cupcake with swirled frosting"/>
    <rect class="doodle" x="228" y="358" width="91" height="82" rx="10" role="img" aria-label="Line drawing of a layered cake slice with candles"/>
    <rect class="doodle" x="878" y="223" width="68" height="51" rx="8" role="img" aria-label="Line drawing of a cake wedge"/>
    <rect class="doodle" x="972" y="331" width="94" height="89" rx="26" role="img" aria-label="Line drawing of stacked heart-shaped cakes"/>

    <polygon class="fun-star" points="294,252 299.9,266.9 315.9,267.9 303.5,278.1 307.5,293.6 294,285 280.5,293.6 284.5,278.1 272.1,267.9 288.1,266.9"/>
    <polygon class="fun-star" points="166,350 170.4,361.2 182.4,362 173.1,369.6 176.1,381.2 166,374.8 155.9,381.2 158.9,369.6 149.6,362 161.6,361.2"/>
    <polygon class="fun-star" points="1034,230 1039.9,244.9 1055.9,245.9 1043.5,256.1 1047.5,271.6 1034,263 1020.5,271.6 1024.5,256.1 1012.1,245.9 1028.1,244.9"/>
    <polygon class="fun-star" points="886,351 891.6,365.1 906.7,366 895,375.7 898.8,390.4 886,382.3 873.2,390.4 877,375.7 865.3,366 880.4,365.1"/>

    <g class="badge">
      <circle class="badge-edge" cx="600" cy="190" r="252"/>
      <circle class="badge-ring" cx="600" cy="190" r="242"/>
      <circle class="badge-dots" cx="600" cy="190" r="230"/>
      <circle class="badge-center" cx="600" cy="190" r="218"/>
      <circle class="badge-rule" cx="600" cy="190" r="211"/>

      <text class="bakery-name" x="600" y="286">The Willow</text>
      <text class="bakery-name" x="600" y="350">Lantern</text>
    </g>
  </g>
</svg>
</body>
</html>
```